Banner signature

Hi, looking for a banner for email signature 728 px wide and 200 px high
Could we have our 10 year logo and premium logo, a similar look and feel of our previous banner design (I've attached) and also include an aboriginal design with the Wording
This email comes to you from Gubbi Gubbi country
I've attached an example of some look and feels that we like.
Can we have the background of banner the Blue colour of our Fern & Tide logo and

```html
<!DOCTYPE html>
<html lang="en">
<head>
<meta charset="UTF-8">
<title>Email Signature Banner – Gubbi Gubbi Country</title>
<link href="https://fonts.googleapis.com/css2?family=Kalam:wght@700&family=Permanent+Marker&display=swap" rel="stylesheet">
<style>
  :root {
    --page-bg: #1f1f1f;
    --sky-blue: #03b0f0;
    --deep-blue: #14317f;
    --white: #ffffff;
    --sun-yellow: #ffec00;
    --soft-yellow: #fff35c;
    --ochre-orange: #f47a20;
    --gold: #d9a92b;
    --ring-rose: #c86a8c;
    --ring-navy: #2b3f8f;
  }
  * { margin: 0; padding: 0; box-sizing: border-box; }
  html, body {
    width: 1200px;
    height: 710px;
    overflow: hidden;
    background: var(--page-bg);
  }
  .banner {
    position: absolute;
    left: 50px;
    top: 228px;
    width: 1100px;
    height: 254px;
    background: var(--sky-blue);
    overflow: hidden;
  }
  .banner-shapes {
    position: absolute;
    inset: 0;
  }
  .premium-brand {
    position: absolute;
    left: 42px;
    top: 18px;
    width: 140px;
    height: 104px;
    display: flex;
    flex-direction: column;
    align-items: center;
    justify-content: center;
    gap: 6px;
  }
  .premium-brand .brand-dot {
    width: 50px;
    height: 50px;
    border-radius: 50%;
    background: var(--gold);
  }
  .premium-brand .brand-name {
    font-family: "Kalam", "Comic Sans MS", sans-serif;
    font-weight: 700;
    font-size: 19px;
    line-height: 1;
    color: var(--deep-blue);
    white-space: nowrap;
  }
  .country-message {
    position: absolute;
    left: 165px;
    top: 20px;
    width: 470px;
    text-align: center;
    white-space: nowrap;
  }
  .country-message .intro {
    font-family: "Kalam", "Comic Sans MS", sans-serif;
    font-weight: 700;
    font-size: 28px;
    line-height: 1.1;
    color: var(--white);
  }
  .country-message .nation {
    font-family: "Permanent Marker", "Kalam", "Comic Sans MS", sans-serif;
    font-size: 70px;
    line-height: 1;
    color: var(--white);
    margin-top: 12px;
    text-shadow: 3px 4px 0 var(--deep-blue), 5px 6px 0 var(--deep-blue);
  }
  .country-message .country {
    font-family: "Permanent Marker", "Kalam", "Comic Sans MS", sans-serif;
    font-size: 54px;
    line-height: 1;
    color: var(--sun-yellow);
    margin-top: 8px;
    margin-right: 34px;
    text-shadow: 2px 3px 0 var(--deep-blue);
  }
  .anniversary-brand {
    position: absolute;
    left: 749px;
    top: 10px;
    width: 240px;
    height: 240px;
    display: flex;
    align-items: center;
    justify-content: center;
  }
  .anniversary-brand .brand-name {
    font-family: "Kalam", "Comic Sans MS", sans-serif;
    font-weight: 700;
    font-size: 30px;
    line-height: 1;
    color: var(--deep-blue);
    white-space: nowrap;
  }
</style>
</head>
<body>
  <div class="banner">
    <svg class="banner-shapes" width="1100" height="254" viewBox="0 0 1100 254" xmlns="http://www.w3.org/2000/svg">
      <defs>
        <radialGradient id="ringTones" cx="50%" cy="50%" r="50%">
          <stop offset="0.55" stop-color="#ffffff"/>
          <stop offset="0.7" stop-color="#c86a8c"/>
          <stop offset="0.85" stop-color="#2b3f8f"/>
          <stop offset="1" stop-color="#f47a20"/>
        </radialGradient>
      </defs>
      <path class="yellow-wave" d="M0 84 C70 80 130 120 175 170 C200 200 218 230 232 254 L0 254 Z" fill="var(--sun-yellow)"/>
      <path d="M0 150 C40 150 80 180 110 220 L120 254 L0 254 Z" fill="var(--soft-yellow)" opacity="0.5"/>
      <circle class="logo-circle" cx="112" cy="60" r="76" fill="var(--white)"/>
      <path class="orange-blob" d="M528 254 C520 210 548 172 596 170 C636 168 658 200 654 254 Z" fill="var(--ochre-orange)"/>
      <path d="M1100 0 L1068 0 L1100 48 Z" fill="var(--white)"/>
      <path d="M1100 130 L1060 254 L1100 254 Z" fill="var(--white)"/>
      <circle cx="872" cy="122" r="228" fill="url(#ringTones)" role="img" aria-label="Aboriginal dot and dash ring artwork in navy, rose, orange and white"/>
      <circle cx="869" cy="130" r="120" fill="var(--gold)"/>
    </svg>

    <div class="premium-brand">
      <div class="brand-dot"></div>
      <div class="brand-name">Fern &amp; Tide</div>
    </div>

    <div class="country-message">
      <p class="intro">This email comes to you from</p>
      <p class="nation">Gubbi Gubbi</p>
      <p class="country">Country</p>
    </div>

    <div class="anniversary-brand">
      <span class="brand-name">Fern &amp; Tide</span>
    </div>
  </div>
</body>
</html>
```